Website Design for a "Talent Recruitment Agency"

We are looking for a website design for the website of our "Talent Recruitment Agency"; which is called "Crestline Circle".
Our recruitment website "Crestline Circle" will be focusing on: "Crestline Circle: Bridging People & Employers in Switzerland"; which means our target audience is two-folded:
(i) TALENT - that is currently residing in- or outside of Switzerland, and is open for and interested in the "Swiss Job Market".
(ii) COMPANIES - that are looking for talent for specific job vacancies in Switzerland.
With our "Crestline Circle" approach we inted to focus on Membership & Partnership:
(a)"Membership"(TALENT)
and
(b)"Partnership"(COMPANIES)
Some of the competitor sites we like are:
• www.brimlo42.dk
• www.qazet.ch
• www.plovik.ch/en
A sitemap example of our website is attached.
Also attached is a "Crestline Circle" logo in .eps format and one in .jpeg format.
We very much look forward to receive your creative ideas.
Best regards,
Crestline Circle
Crestline Circle: Bridging People & Employers in Switzerland.
Website: crestlinecircle.ch - Twitter: CrestlineCircleCH
Target Market(s)
(i) TALENT (with around 0-10 years of working experience), currently residing in- or outside of Switzerland, but eligible to work in Switzerland.
(ii) COMPANIES (national or international) that are based in Switzerland.
Industry/Entity Type
Recruitment

```html
<!DOCTYPE html>
<html lang="en">
<head>
<meta charset="utf-8">
<title>Crestline Circle – Jobs</title>
<link href="https://fonts.googleapis.com/css2?family=Lato:wght@400;700&family=Open+Sans:wght@400;600&display=swap" rel="stylesheet">
<style>
:root{
  --blue:#1a8fd1;
  --blue-dark:#1479b5;
  --orange:#f26522;
  --text:#333;
  --muted:#555;
  --line:#d6d6d6;
  --panel:#f4f4f4;
  --hero-bg:#e9e9e9;
}
*{margin:0;padding:0;box-sizing:border-box}
html,body{width:842px;height:1200px;overflow:hidden;background:#fff}
body{font-family:'Lato',sans-serif;color:var(--text);position:relative}
.page{position:absolute;left:92px;width:658px;top:0;height:1200px}

/* header */
.site-header{position:relative;height:71px}
.brand{position:absolute;left:0;top:24px;display:flex;align-items:center;gap:8px}
.brand-dot{width:28px;height:28px;border-radius:50%;background:var(--blue)}
.brand-name{font-family:'Lato',sans-serif;font-weight:700;font-size:21px;color:var(--orange)}
.lang{position:absolute;right:0;top:12px;font-size:10px;color:var(--muted);display:flex;align-items:center;gap:4px}
.lang svg{display:block}
.contact-line{position:absolute;right:0;top:39px;display:flex;align-items:center;gap:14px;font-size:11px;color:var(--muted)}
.contact-line .phone{font-size:12px;letter-spacing:.5px}
.contact-line span{display:flex;align-items:center;gap:6px}

/* nav */
.main-nav{display:flex;height:30px;background:var(--blue)}
.main-nav a{color:#fff;text-decoration:none;font-size:10.5px;font-weight:700;display:flex;align-items:center;justify-content:center;border-right:1px solid var(--blue-dark)}
.main-nav a:last-child{border-right:0}
.main-nav a.active{background:var(--orange)}

/* hero */
.hero{height:131px;background:var(--hero-bg);position:relative}
.hero-photo{position:absolute;left:0;top:0;width:316px;height:131px;background:linear-gradient(100deg,#c7c9cf 0%,#dcd6d0 45%,#ebe7e4 100%)}

/* listing */
.page-title{margin-top:16px;font-family:'Open Sans',sans-serif;font-size:16px;font-weight:400;color:var(--blue);padding-bottom:6px;border-bottom:2px solid var(--line)}
.list-tools{display:flex;justify-content:space-between;align-items:center;margin-top:8px;height:18px;font-size:9px;color:var(--muted)}
.list-tools .show{display:flex;align-items:center;gap:6px;padding-left:2px}
.select{width:33px;height:17px;border:1px solid var(--line);display:flex;align-items:center;justify-content:space-between;padding:0 3px;font-size:8.5px;background:#fff}
.search{display:flex;align-items:center;gap:4px}
.search .field{width:116px;height:17px;border:1px solid var(--line);background:#fff}

.jobs{list-style:none;margin-top:12px}
.job{position:relative;height:53px;margin-bottom:19.4px;border:1px solid var(--line);background:linear-gradient(#fafafa,#f1f1f1);box-shadow:0 5px 6px -5px rgba(0,0,0,.18);padding:6px 0 0 31px}
.job-num{position:absolute;left:7px;top:8px;width:16px;height:16px;border-radius:50%;background:#ddd;font-size:9px;color:#444;display:flex;align-items:center;justify-content:center}
.job-title{font-family:'Open Sans',sans-serif;font-size:10px;font-weight:600;color:var(--orange);letter-spacing:.2px}
.job-title em{font-style:normal;font-weight:400;color:var(--blue);margin-left:5px}
.job-desc{font-size:8.4px;line-height:14px;color:var(--text);width:550px;margin-top:0}
.read-more{position:absolute;right:6px;top:16px;width:67px;height:24px;background:var(--blue);color:#fff;font-size:12px;font-weight:700;display:flex;align-items:center;justify-content:center;text-decoration:none}

.pager{position:absolute;left:0;right:0;top:1040px;height:34px;background:var(--panel);display:flex;align-items:center;justify-content:space-between;padding:0 7px;font-size:9px;color:var(--text)}
.pager .pages{display:flex;gap:8px}
.pager .pages span{height:16px;min-width:18px;padding:0 7px;background:#ddd;display:flex;align-items:center;justify-content:center;font-size:10px}
.pager .pages .current{background:var(--blue);color:#fff}

/* footer */
.site-footer{position:absolute;left:0;right:0;top:1100px;height:100px;background:var(--blue);border-top:2px solid var(--orange);color:#fff;text-align:center}
.footer-nav{margin-top:8px;font-size:9.5px;font-weight:700}
.footer-nav a{color:#fff;text-decoration:none;margin:0 5px}
.footer-contact{display:flex;justify-content:center;gap:18px;margin-top:8px;font-size:8.5px;font-weight:700;text-align:left}
.footer-contact span{display:flex;align-items:flex-start;gap:6px}
.socials{display:flex;justify-content:center;gap:7px;margin-top:4px}
.socials i{width:20px;height:20px;border-radius:50%;background:#fff;display:block}
.copyright{position:absolute;left:0;right:0;bottom:0;height:24px;border-top:1px solid var(--blue-dark);font-size:9px;display:flex;align-items:center;justify-content:center}
</style>
</head>
<body>
<div class="page">
  <header class="site-header">
    <div class="brand"><span class="brand-dot"></span><span class="brand-name">Crestline Circle</span></div>
    <div class="lang">Multi-language Support:
      <svg width="20" height="14" viewBox="0 0 20 14" aria-label="English"><rect width="20" height="14" fill="#1f3b7a"/><rect x="8" width="4" height="14" fill="#fff"/><rect y="5" width="20" height="4" fill="#fff"/><rect x="8.8" width="2.4" height="14" fill="#c8202f"/><rect y="5.8" width="20" height="2.4" fill="#c8202f"/></svg>
      <svg width="20" height="14" viewBox="0 0 20 14" aria-label="Deutsch"><rect width="20" height="4.7" fill="#000"/><rect y="4.7" width="20" height="4.7" fill="#dd0000"/><rect y="9.4" width="20" height="4.6" fill="#ffce00"/></svg>
    </div>
    <div class="contact-line">
      <span class="phone"><svg width="11" height="11" viewBox="0 0 24 24"><path fill="#f26522" d="M6.6 10.8a15.1 15.1 0 006.6 6.6l2.2-2.2c.3-.3.7-.4 1-.2 1.1.4 2.3.6 3.6.6.6 0 1 .4 1 1V20c0 .6-.4 1-1 1A17 17 0 013 4c0-.6.4-1 1-1h3.5c.6 0 1 .4 1 1 0 1.3.2 2.5.6 3.6.1.3 0 .7-.2 1z"/></svg>(123) 555 0142</span>
      <span><svg width="11" height="8" viewBox="0 0 11 8"><rect width="11" height="8" fill="#f26522"/><path d="M0 0l5.5 4.5L11 0" stroke="#fff" fill="none"/></svg>info@crestlinecircle.ch</span>
    </div>
  </header>

  <nav class="main-nav">
    <a style="width:92px">HOME</a><a style="width:111px">ABOUT</a><a style="width:113px">TALENT</a><a style="width:136px">COMPANIES</a><a class="active" style="width:98px">JOBS</a><a style="width:108px">CONTACT</a>
  </nav>

  <section class="hero">
    <div class="hero-photo" role="img" aria-label="Photo of a smiling young professional giving a thumbs up, with celebrating colleagues behind her"></div>
  </section>

  <h1 class="page-title">Jobs</h1>
  <div class="list-tools">
    <div class="show">Show <span class="select">10 <svg width="6" height="4" viewBox="0 0 6 4"><path d="M0 0h6L3 4z" fill="#333"/></svg></span> Opportunities</div>
    <div class="search">Search : <span class="field"></span></div>
  </div>

  <ol class="jobs">
    <li class="job"><span class="job-num">1</span><div class="job-title">Lorem ipsaerum dolor sit amet.<em>(Dolor sit amet)</em></div><p class="job-desc">Lorem ipsum dolor sit amet, consectetuer adipiscing elit, sed diam nonummy n euismod tincidunt ut laoreet dolore magn aliq volutpat. Ut wisi enim ad minim veniam, quis nostrud exerci tation ullamcorper suscipit lobortis nisl ut aliquip ex commodo consequat.</p><a class="read-more">Read More</a></li>
    <li class="job"><span class="job-num">2</span><div class="job-title">Quis nostrud exerci tation ullamcorper<em>(Consectetuer adipiscing)</em></div><p class="job-desc">Lorem ipsum dolor sit amet, consectetuer adipiscing elit, sed diam nonummy n euismod tincidunt ut laoreet dolore magn aliq volutpat. Ut wisi enim ad minim veniam, quis nostrud exerci tation ullamcorper suscipit lobortis nisl ut aliquip ex commodo consequat.</p><a class="read-more">Read More</a></li>
    <li class="job"><span class="job-num">3</span><div class="job-title">Ullamcorper suscipit lobortis<em>(Enim ad minim veniam)</em></div><p class="job-desc">Lorem ipsum dolor sit amet, consectetuer adipiscing elit, sed diam nonummy n euismod tincidunt ut laoreet dolore magn aliq volutpat. Ut wisi enim ad minim veniam, quis nostrud exerci tation ullamcorper suscipit lobortis nisl ut aliquip ex commodo consequat.</p><a class="read-more">Read More</a></li>
    <li class="job"><span class="job-num">4</span><div class="job-title">laoreet dolore magn aliq volutpat.<em>(Consectetuer adipiscing)</em></div><p class="job-desc">Lorem ipsum dolor sit amet, consectetuer adipiscing elit, sed diam nonummy n euismod tincidunt ut laoreet dolore magn aliq volutpat. Ut wisi enim ad minim veniam, quis nostrud exerci tation ullamcorper suscipit lobortis nisl ut aliquip ex commodo consequat.</p><a class="read-more">Read More</a></li>
    <li class="job"><span class="job-num">5</span><div class="job-title">Lorem ipsaerum dolor sit amet.<em>(Dolor sit amet)</em></div><p class="job-desc">Lorem ipsum dolor sit amet, consectetuer adipiscing elit, sed diam nonummy n euismod tincidunt ut laoreet dolore magn aliq volutpat. Ut wisi enim ad minim veniam, quis nostrud exerci tation ullamcorper suscipit lobortis nisl ut aliquip ex commodo consequat.</p><a class="read-more">Read More</a></li>
    <li class="job"><span class="job-num">6</span><div class="job-title">Quis nostrud exerci tation ullamcorper<em>(Consectetuer adipiscing)</em></div><p class="job-desc">Lorem ipsum dolor sit amet, consectetuer adipiscing elit, sed diam nonummy n euismod tincidunt ut laoreet dolore magn aliq volutpat. Ut wisi enim ad minim veniam, quis nostrud exerci tation ullamcorper suscipit lobortis nisl ut aliquip ex commodo consequat.</p><a class="read-more">Read More</a></li>
    <li class="job"><span class="job-num">7</span><div class="job-title">Ullamcorper suscipit lobortis<em>(Enim ad minim veniam)</em></div><p class="job-desc">Lorem ipsum dolor sit amet, consectetuer adipiscing elit, sed diam nonummy n euismod tincidunt ut laoreet dolore magn aliq volutpat. Ut wisi enim ad minim veniam, quis nostrud exerci tation ullamcorper suscipit lobortis nisl ut aliquip ex commodo consequat.</p><a class="read-more">Read More</a></li>
    <li class="job"><span class="job-num">8</span><div class="job-title">laoreet dolore magn aliq volutpat.<em>(Consectetuer adipiscing)</em></div><p class="job-desc">Lorem ipsum dolor sit amet, consectetuer adipiscing elit, sed diam nonummy n euismod tincidunt ut laoreet dolore magn aliq volutpat. Ut wisi enim ad minim veniam, quis nostrud exerci tation ullamcorper suscipit lobortis nisl ut aliquip ex commodo consequat.</p><a class="read-more">Read More</a></li>
    <li class="job"><span class="job-num">9</span><div class="job-title">laoreet dolore magn aliq volutpat.<em>(Consectetuer adipiscing)</em></div><p class="job-desc">Lorem ipsum dolor sit amet, consectetuer adipiscing elit, sed diam nonummy n euismod tincidunt ut laoreet dolore magn aliq volutpat. Ut wisi enim ad minim veniam, quis nostrud exerci tation ullamcorper suscipit lobortis nisl ut aliquip ex commodo consequat.</p><a class="read-more">Read More</a></li>
    <li class="job"><span class="job-num">10</span><div class="job-title">Ullamcorper suscipit lobortis<em>(Enim ad minim veniam)</em></div><p class="job-desc">Lorem ipsum dolor sit amet, consectetuer adipiscing elit, sed diam nonummy n euismod tincidunt ut laoreet dolore magn aliq volutpat. Ut wisi enim ad minim veniam, quis nostrud exerci tation ullamcorper suscipit lobortis nisl ut aliquip ex commodo consequat.</p><a class="read-more">Read More</a></li>
  </ol>

  <div class="pager">
    <span>Showing 1 - 10 of 12 &nbsp;Opportunities</span>
    <div class="pages"><span class="current">1</span><span>2</span><span>Next</span><span>Last</span></div>
  </div>

  <footer class="site-footer">
    <nav class="footer-nav"><a>HOME</a>|<a>ABOUT</a>|<a>TALENT</a>|<a>COMPANIES</a>|<a>JOBS</a>|<a>EVENTS</a>|<a>CONTACT</a></nav>
    <div class="footer-contact">
      <span><svg width="12" height="11" viewBox="0 0 12 11"><path d="M6 0L0 5h1.5v6h3.5V7.5h2V11h3.5V5H12z" fill="#f26522"/></svg>Lorem ipsum dolor sit amet, adipiscing<br>elit,</span>
      <span><svg width="12" height="12" viewBox="0 0 12 12"><circle cx="6" cy="6" r="5.3" fill="none" stroke="#f26522" stroke-width="1.2"/><path d="M4.3 3.3l1 1.6-.6.6c.4.8 1 1.4 1.8 1.8l.6-.6 1.6 1-.6 1.1C5.6 8.6 3.6 6.6 3.3 4z" fill="#f26522"/></svg>123.555.0142</span>
      <span><svg width="12" height="12" viewBox="0 0 12 12"><circle cx="6" cy="6" r="5.3" fill="none" stroke="#f26522" stroke-width="1.2"/><circle cx="6" cy="6" r="2" fill="none" stroke="#f26522" stroke-width="1.2"/></svg>info@crestlinecircle.ch</span>
    </div>
    <div class="socials"><i></i><i></i><i></i><i></i></div>
    <div class="copyright">© 2014 Crestline Circle. All Right Reserved. &nbsp;T&amp;Cs &nbsp;&nbsp;| Disclaimer</div>
  </footer>
</div>
</body>
</html>
```